Graphik für Bewerbungs-Coaching gesucht
Zielgruppe
Ich bin Karriere-Coach und biete Bewerbungs-Coaching, berufliche Neuorientierung und Personal Branding an. Meine Zielgruppe sind primär Männer aus dem technischen Bereich zwischen 30 und 55 aus dem mittleren Management.
Aufgabenstellung
Das Design soll sowohl in Farbe als auch in s/w wirken. Ich möchte es als Graphik in mein Buch einfügen, es aber auch auf Social Media nutzen können. Ein eher quadratisches Layout wäre deswegen von Vorteil. Das Layout sollte farblich zu meiner Homepage www.varnemo.de passen.
Die beigefügte Skizze verdeutlicht, wie die Graphik aussehen könnte. Für andere Darstellungsformen bin ich offen. Der Text sollte genauso übernommen werden.
Gern darf der Hintergrund auch farbig sein.

```html
<!DOCTYPE html>
<html lang="de">
<head>
<meta charset="utf-8">
<title>Kopf, Herz, Bauch, Hand</title>
<link rel="stylesheet" href="https://fonts.googleapis.com/css2?family=Source+Sans+3:wght@400;700&display=swap">
<style>
  :root {
    --teal: #04a99d;
    --ink: #000000;
    --figure: #333333;
    --paper: #ffffff;
  }
  html, body {
    margin: 0;
    padding: 0;
    overflow: hidden;
    background: var(--paper);
  }
  .canvas {
    width: 1200px;
    height: 1200px;
    display: block;
    font-family: "Source Sans 3", "Myriad Pro", sans-serif;
  }
  .connector { stroke: var(--teal); stroke-width: 5; fill: none; }
  .node, .badge { fill: var(--teal); }
  .icon { fill: none; stroke: var(--paper); stroke-width: 5.5; stroke-linecap: round; stroke-linejoin: round; }
  .figure { fill: var(--figure); }
  .label-title { font-weight: 700; font-size: 37px; fill: var(--ink); }
  .label-rule { fill: var(--teal); }
  .label-text { font-weight: 400; font-size: 33px; fill: var(--ink); }
</style>
</head>
<body>
<svg class="canvas" viewBox="0 0 1200 1200" xmlns="http://www.w3.org/2000/svg">

  <!-- Central person area -->
  <rect class="figure" x="477" y="326" width="198" height="583" rx="60"
        role="img" aria-label="Silhouette eines stehenden Mannes in Frontansicht"/>

  <!-- Connectors -->
  <line class="connector" x1="212" y1="272" x2="567" y2="464"/>
  <line class="connector" x1="628" y1="323" x2="794" y2="257"/>
  <line class="connector" x1="217" y1="829" x2="559" y2="614"/>
  <line class="connector" x1="698" y1="663" x2="830" y2="789"/>

  <!-- Body points -->
  <circle class="node" cx="599" cy="339" r="32.5"/>
  <circle class="node" cx="595" cy="481" r="32.5"/>
  <circle class="node" cx="579" cy="591" r="32.5"/>
  <circle class="node" cx="669" cy="649" r="32.5"/>

  <!-- Herz badge -->
  <g transform="translate(147.5 232)">
    <circle class="badge" r="75.5"/>
    <path class="icon" d="M0,40 L-40,0 A22,22 0 1 1 0,-26 A22,22 0 1 1 40,0 Z"/>
  </g>

  <!-- Kopf badge -->
  <g transform="translate(863 232)">
    <circle class="badge" r="75.5"/>
    <path class="icon" d="M0,-40 C-10,-48 -24,-44 -26,-34 C-38,-34 -44,-22 -38,-12 C-48,-4 -46,12 -36,16 C-38,30 -24,40 -14,36 C-8,46 0,44 0,40 Z"/>
    <path class="icon" d="M0,-40 C10,-48 24,-44 26,-34 C38,-34 44,-22 38,-12 C48,-4 46,12 36,16 C38,30 24,40 14,36 C8,46 0,44 0,40 Z"/>
    <path class="icon" d="M0,-40 V40 M-18,-20 C-22,-12 -12,-8 -14,2 M-28,14 C-20,16 -14,10 -12,18 M18,-20 C22,-12 12,-8 14,2 M28,14 C20,16 14,10 12,18"/>
  </g>

  <!-- Bauch badge -->
  <g transform="translate(147.5 856)">
    <circle class="badge" r="75.5"/>
    <path class="icon" d="M0,-40 V-32 Q0,-24 -8,-24 H-27 A9,9 0 0 0 -27,-6 H27 A9,9 0 0 1 27,12 H-27 A9,9 0 0 0 -27,30 H0 Q-8,30 -8,38 V44"/>
  </g>

  <!-- Hand badge -->
  <g transform="translate(873 851)">
    <circle class="badge" r="75.5"/>
    <path class="icon" d="M-28,22 V-20 A5,5 0 0 1 -18,-20 V-4 M-18,-4 V-34 A5,5 0 0 1 -8,-34 V-4 M-8,-4 V-40 A5,5 0 0 1 2,-40 V-4 M2,-4 V-34 A5,5 0 0 1 12,-34 V6 L22,-8 A5,5 0 0 1 30,-2 L14,28 Q4,44 -10,44 Q-28,44 -28,22"/>
  </g>

  <!-- Labels -->
  <g class="label">
    <text class="label-title" x="89" y="377">Herz</text>
    <rect class="label-rule" x="91" y="385" width="90" height="5"/>
    <text class="label-text" x="89" y="431">Emotionen,</text>
    <text class="label-text" x="89" y="478">Leidenschaft, Freude</text>
  </g>

  <g class="label">
    <text class="label-title" x="818" y="375">Kopf</text>
    <rect class="label-rule" x="820" y="384" width="89" height="5"/>
    <text class="label-text" x="818" y="430">Zahlen, Daten, Fakten</text>
  </g>

  <g class="label">
    <text class="label-title" x="85" y="993">Bauch</text>
    <rect class="label-rule" x="87" y="1001" width="89" height="5"/>
    <text class="label-text" x="85" y="1048">Wertvorstellungen</text>
  </g>

  <g class="label">
    <text class="label-title" x="817" y="993">Hand</text>
    <rect class="label-rule" x="819" y="1001" width="89" height="5"/>
    <text class="label-text" x="817" y="1048">Greifbare Beispiele</text>
  </g>
</svg>
</body>
</html>
```